Ridgewell Stonecraft Construction Needs business card

Hey we are in need of business card designs. I have upload our logo as a guideline, but free feel to run with it or come up with something unique.
Pls have fun with it and be creative. the name says it all!
i will give some directions after i see a few entries..
Logo source file has been uploaded..
Hey because of the logo is so colourful already.
Can we have a few submissions with less colour.
Also we are looking for clever/hidden/descriptive business card.

```html
<!DOCTYPE html>
<html lang="en">
<head>
<meta charset="utf-8">
<title>Ridgewell Stonecraft Construction – Business Card</title>
<link rel="stylesheet" href="https://fonts.googleapis.com/css2?family=Arimo:wght@400;700&display=swap">
<style>
  :root {
    --backdrop: #e9e6e1;
    --card: #ffffff;
    --ink: #1e1e1e;
    --ink-soft: #3c3c3c;
    --wordmark: #6f6f6f;
    --accent-blue: #3d63c9;
    --tile-yellow: #e8d67a;
    --tile-orange: #e98b5e;
    --tile-blue: #8aa7d6;
    --tile-green: #7cc39a;
    --tile-grey: #8c8c8c;
    --tile-red: #e0503c;
    --tile-cyan: #3aa9de;
  }
  * { box-sizing: border-box; margin: 0; padding: 0; }
  html, body {
    width: 1200px; height: 800px; overflow: hidden;
    background: var(--backdrop);
    font-family: "Arimo", Arial, sans-serif;
  }
  .sheet {
    width: 1200px; height: 800px;
    display: flex; align-items: center; justify-content: center; gap: 40px;
  }
  .card {
    position: relative;
    width: 540px; height: 308px;
    background: var(--card);
    box-shadow: 0 2px 10px rgba(0,0,0,.12);
    overflow: hidden;
  }

  /* Front */
  .brand {
    position: absolute; left: 40px; top: 72px;
    display: flex; align-items: center; gap: 10px;
  }
  .brand-square { width: 16px; height: 16px; background: var(--accent-blue); flex: none; }
  .brand-name {
    font-size: 18px; font-weight: 400; color: var(--wordmark);
    text-transform: uppercase; letter-spacing: .4px; line-height: 1;
    white-space: nowrap;
  }
  .brand-sub {
    position: absolute; left: 66px; top: 96px;
    font-size: 8px; letter-spacing: 2px; color: var(--wordmark); text-transform: uppercase;
  }
  .contact {
    position: absolute; left: 66px; top: 138px;
    color: var(--ink); font-size: 10.5px; line-height: 1.45;
  }
  .contact .person { font-size: 14px; font-weight: 700; }
  .contact .role { font-size: 10px; color: var(--ink-soft); margin-bottom: 12px; }
  .contact .address { margin-bottom: 12px; }
  .contact-line { display: flex; align-items: center; gap: 8px; }
  .contact-line svg { width: 10px; height: 10px; fill: var(--ink); flex: none; }
  .tile-field {
    position: absolute; right: 20px; top: 20px;
    width: 170px; height: 150px;
    background: linear-gradient(135deg, var(--tile-yellow) 0%, var(--tile-orange) 35%, var(--tile-blue) 65%, var(--tile-grey) 100%);
    opacity: .7;
  }

  /* Back */
  .mosaic-band {
    position: absolute; left: 0; top: 0; width: 540px; height: 308px;
    background: linear-gradient(160deg, var(--tile-red) 0%, var(--tile-green) 30%, var(--tile-cyan) 55%, var(--accent-blue) 80%, var(--tile-orange) 100%);
    opacity: .55;
  }
  .back-mark {
    position: absolute; left: 0; right: 0; top: 104px;
    text-align: center; background: rgba(255,255,255,.88); padding: 18px 0 14px;
  }
  .back-name {
    font-size: 32px; font-weight: 400; color: var(--wordmark);
    text-transform: uppercase; letter-spacing: 1px; line-height: 1;
  }
  .back-sub {
    margin-top: 6px; font-size: 11px; letter-spacing: 4px; color: var(--wordmark); text-transform: uppercase;
  }
  .back-web {
    position: absolute; right: 22px; bottom: 16px;
    font-size: 10px; color: var(--ink-soft); background: rgba(255,255,255,.88); padding: 2px 6px;
  }
</style>
</head>
<body>
<main class="sheet">
  <section class="card card-front" aria-label="Business card front">
    <div class="brand">
      <span class="brand-square"></span>
      <span class="brand-name">Ridgewell Stonecraft</span>
    </div>
    <div class="brand-sub">Construction</div>

    <div class="contact">
      <div class="person">Dario Halvorsen</div>
      <div class="role">Director</div>
      <div class="address">Jalan Melati 27B, Kebon Sari<br>Jakarta Timur - Indonesia 13210</div>
      <div class="contact-line">
        <svg viewBox="0 0 10 10"><path d="M2 0.5 L3.6 2.6 L2.8 3.6 C3.4 5 4.9 6.5 6.4 7.2 L7.4 6.4 L9.5 8 L8.4 9.5 C4.6 9 1 5.4 0.5 1.6 Z"/></svg>
        <span>+62 (21) 555.014.2277</span>
      </div>
      <div class="contact-line">
        <svg viewBox="0 0 10 10"><path d="M2.5 0 H7.5 V10 H2.5 Z M3.3 1 V8 H6.7 V1 Z"/></svg>
        <span>+62 (08) 5550.193.4821</span>
      </div>
      <div class="contact-line">
        <svg viewBox="0 0 10 10"><path d="M0 2 H10 V8.5 H0 Z M0.8 2.6 L5 5.8 L9.2 2.6"/></svg>
        <span>dario@ridgewellstonecraft.com</span>
      </div>
    </div>

    <div class="tile-field" role="img" aria-label="Scattered tilted coloured squares decoration"></div>
  </section>

  <section class="card card-back" aria-label="Business card back">
    <div class="mosaic-band" role="img" aria-label="Multicoloured square tile mosaic pattern"></div>
    <div class="back-mark">
      <div class="back-name">Ridgewell Stonecraft</div>
      <div class="back-sub">Construction</div>
    </div>
    <div class="back-web">www.ridgewellstonecraft.com</div>
  </section>
</main>
</body>
</html>
```